Business Card Design Project for New Home Builder

Double sided card,
Larger logo on 1 side with small quote, Its not just a house, Its your Home, across the bottom. Matt Red base, White logo, black quote??

other side, ,
Its your Home LHS. Smaller logo RHS with.
Details below.

"neuropolitical Rg" Logo Font

Dennis Orford

PO Box 8437 Mildura VIC 3502
Mobile 0427 318865 / Phone 03 50718 962 / Fax 03 50718 415
email DennisO@tbvbuild.net.au
Vic Building Practitioner DB-U 8174 Vic Commercial Builder CB-U 5093
NSW Contractor Reg 37086C

Target Market(s)

New Home Buyers

Industry/Entity Type

Business

Requirements
Must have
• Sharp detail, Red Black & White colourings.
Should not have
• Any new colours

```html
<!DOCTYPE html>
<html lang="en">
<head>
<meta charset="utf-8">
<title>Dennis Orford Homes – Business Card</title>
<link rel="stylesheet" href="https://fonts.googleapis.com/css2?family=Cinzel:wght@400;700&display=swap">
<style>
  :root {
    --ink: #0b0b0b;
    --paper: #ffffff;
    --paper-shade: #ececec;
    --red: #e8323a;
    --silver-light: #f4f4f4;
    --silver-dark: #8a8a8a;
    --backdrop: #d9d9d9;
  }
  * { margin: 0; padding: 0; box-sizing: border-box; }
  html, body { width: 1200px; height: 900px; overflow: hidden; }
  body {
    background: var(--backdrop);
    font-family: "Cinzel", serif;
    position: relative;
  }
  .card {
    position: absolute;
    left: 250px;
    width: 700px;
    height: 400px;
    border-radius: 30px;
    overflow: hidden;
    box-shadow: 0 10px 24px rgba(0,0,0,0.25);
  }
  .card--details { top: 30px; }
  .card--logo { top: 470px; }
  .card__art { position: absolute; inset: 0; width: 100%; height: 100%; }

  .brand {
    position: absolute;
    display: flex;
    align-items: center;
    gap: 12px;
    color: var(--ink);
    font-family: "Cinzel", serif;
    font-weight: 700;
    text-transform: uppercase;
    line-height: 1.05;
  }
  .brand__mark { width: 16px; height: 16px; background: var(--red); flex: none; }
  .brand__name { font-size: 28px; letter-spacing: 1px; }
  .brand__name small { display: block; font-size: 13px; letter-spacing: 6px; text-align: center; }

  .card--details .brand { left: 40px; top: 165px; }
  .card--logo .brand { left: 230px; top: 140px; }
  .card--logo .brand__name { font-size: 26px; }

  .person {
    position: absolute;
    left: 440px;
    top: 70px;
    color: var(--paper);
    font-variant: small-caps;
    letter-spacing: 1px;
  }
  .person__name { font-size: 24px; font-weight: 400; }
  .person__role { font-size: 19px; margin-top: 2px; }

  .contact {
    position: absolute;
    left: 420px;
    top: 208px;
    list-style: none;
    color: var(--paper);
    font-size: 13px;
    font-variant: small-caps;
    line-height: 17px;
  }
  .contact__item { display: flex; align-items: flex-start; gap: 7px; }
  .contact__icon { width: 13px; height: 13px; flex: none; margin-top: 2px; }
  .contact__item--licence { padding-left: 20px; font-size: 12px; }

  .tagline {
    position: absolute;
    left: 34px;
    bottom: 24px;
    color: var(--paper);
    font-size: 13px;
    line-height: 18px;
    letter-spacing: 1px;
    font-variant: small-caps;
  }
</style>
</head>
<body>

<section class="card card--details" aria-label="Business card, details side">
  <svg class="card__art" viewBox="0 0 700 400" aria-hidden="true">
    <defs>
      <linearGradient id="silver" x1="0" y1="0" x2="1" y2="1">
        <stop offset="0" stop-color="var(--silver-dark)"/>
        <stop offset="0.5" stop-color="var(--silver-light)"/>
        <stop offset="1" stop-color="var(--silver-dark)"/>
      </linearGradient>
      <radialGradient id="paper-sheen" cx="0.35" cy="0.4" r="0.7">
        <stop offset="0" stop-color="var(--paper)"/>
        <stop offset="1" stop-color="var(--paper-shade)"/>
      </radialGradient>
    </defs>
    <rect class="base" width="700" height="400" fill="var(--ink)"/>
    <path class="corner-band" d="M600 0 H700 V200 C690 120 670 50 600 0 Z" fill="var(--red)"/>
    <path class="corner-edge" d="M600 0 C670 50 690 120 700 200" fill="none" stroke="url(#silver)" stroke-width="6"/>
    <path class="white-panel" d="M0 0 H320 C430 80 430 280 260 400 H0 Z" fill="url(#paper-sheen)"/>
    <path class="panel-edge" d="M320 0 C430 80 430 280 260 400" fill="none" stroke="url(#silver)" stroke-width="9"/>
  </svg>

  <div class="brand">
    <span class="brand__mark"></span>
    <span class="brand__name">Dennis Orford<small>Homes</small></span>
  </div>

  <div class="person">
    <p class="person__name">Dennis Orford</p>
    <p class="person__role">Owner / C.E.O</p>
  </div>

  <ul class="contact">
    <li class="contact__item">
      <svg class="contact__icon" viewBox="0 0 14 14" aria-hidden="true"><circle cx="7" cy="7" r="7" fill="#fff"/><path d="M7 3a2.5 2.5 0 0 0-2.5 2.5C4.5 7.5 7 11 7 11s2.5-3.5 2.5-5.5A2.5 2.5 0 0 0 7 3z" fill="#0b0b0b"/></svg>
      <span>PO Box 8437 Mildura<br>VIC 3502</span>
    </li>
    <li class="contact__item">
      <svg class="contact__icon" viewBox="0 0 14 14" aria-hidden="true"><circle cx="7" cy="7" r="7" fill="#fff"/><rect x="5" y="3" width="4" height="8" rx="1" fill="#0b0b0b"/></svg>
      <span>0427 318865</span>
    </li>
    <li class="contact__item">
      <svg class="contact__icon" viewBox="0 0 14 14" aria-hidden="true"><circle cx="7" cy="7" r="7" fill="#fff"/><path d="M4 4l2 0 1 2-1 1c.5 1 1 1.5 2 2l1-1 2 1v2c-4 0-7-3-7-7z" fill="#0b0b0b"/></svg>
      <span>03 50718 962</span>
    </li>
    <li class="contact__item">
      <svg class="contact__icon" viewBox="0 0 14 14" aria-hidden="true"><circle cx="7" cy="7" r="7" fill="#fff"/><rect x="3.5" y="5" width="7" height="5" fill="#0b0b0b"/><rect x="5" y="3" width="4" height="2" fill="#0b0b0b"/></svg>
      <span>03 50718 415</span>
    </li>
    <li class="contact__item">
      <svg class="contact__icon" viewBox="0 0 14 14" aria-hidden="true"><circle cx="7" cy="7" r="7" fill="#fff"/><rect x="3" y="4.5" width="8" height="5" fill="#0b0b0b"/><path d="M3 4.5l4 3 4-3" fill="none" stroke="#fff" stroke-width="0.8"/></svg>
      <span>DennisO@tbvbuild.net.au</span>
    </li>
    <li class="contact__item">
      <svg class="contact__icon" viewBox="0 0 14 14" aria-hidden="true"><circle cx="7" cy="7" r="7" fill="#fff"/><circle cx="7" cy="7" r="4" fill="none" stroke="#0b0b0b" stroke-width="1"/><path d="M3 7h8M7 3c-2 2-2 6 0 8M7 3c2 2 2 6 0 8" fill="none" stroke="#0b0b0b" stroke-width="0.8"/></svg>
      <span>www.tbvbuild.net.au</span>
    </li>
    <li class="contact__item contact__item--licence">
      <span>DB-U 8174 · CB-U 5093<br>NSW Reg 37086C</span>
    </li>
  </ul>
</section>

<section class="card card--logo" aria-label="Business card, logo side">
  <svg class="card__art" viewBox="0 0 700 400" aria-hidden="true">
    <defs>
      <linearGradient id="silver-ring" x1="0" y1="0" x2="1" y2="1">
        <stop offset="0" stop-color="var(--silver-light)"/>
        <stop offset="0.5" stop-color="var(--silver-dark)"/>
        <stop offset="1" stop-color="var(--silver-light)"/>
      </linearGradient>
      <radialGradient id="disc-sheen" cx="0.4" cy="0.4" r="0.7">
        <stop offset="0" stop-color="var(--paper)"/>
        <stop offset="1" stop-color="var(--paper-shade)"/>
      </radialGradient>
    </defs>
    <rect class="base" width="700" height="400" fill="var(--ink)"/>
    <path class="corner-band" d="M420 400 C560 370 650 290 700 150 V400 Z" fill="var(--red)"/>
    <path class="corner-edge" d="M420 400 C560 370 650 290 700 150" fill="none" stroke="url(#silver-ring)" stroke-width="6"/>
    <circle class="disc-ring" cx="380" cy="175" r="200" fill="url(#silver-ring)"/>
    <circle class="disc" cx="380" cy="175" r="190" fill="url(#disc-sheen)"/>
  </svg>

  <div class="brand">
    <span class="brand__mark"></span>
    <span class="brand__name">Dennis Orford<small>Homes</small></span>
  </div>

  <p class="tagline">It's not just a house,<br>it's your Home</p>
</section>

</body>
</html>
```